Business Card Design

Hoping for a black background business card, minimalistic design.
With the Marble Crest logo you created in white.

I would like to include:
My Name and title
Address (street address)
Reception: (phone number)
Fax: (fax number)
Reception: (email address)
Direct email: (email address)
Instagram: (ig handle)

```html
<!DOCTYPE html>
<html lang="en">
<head>
<meta charset="utf-8">
<title>Marble Crest Business Card</title>
<link href="https://fonts.googleapis.com/css2?family=Montserrat:wght@500;700&family=Arimo:wght@400;700&display=swap" rel="stylesheet">
<style>
  :root {
    --page: #ececec;
    --card: #2b2b2b;
    --ink: #ffffff;
    --muted: #d6d6d6;
    --faint: #3a3a3a;
    --emboss: #333333;
  }
  * { box-sizing: border-box; margin: 0; padding: 0; }
  html, body { width: 1200px; height: 802px; overflow: hidden; background: var(--page); }
  .canvas { position: relative; width: 1200px; height: 802px; }
  .card {
    position: absolute; top: 241px; width: 560px; height: 320px;
    background: var(--card); overflow: hidden; color: var(--ink);
    box-shadow: 0 6px 18px rgba(0,0,0,.18);
  }
  .card--front { left: 27px; }
  .card--back { left: 613px; }

  .deco-ring { position: absolute; border-radius: 50%; border: 9px solid var(--faint); }
  .card--front .deco-ring { width: 220px; height: 220px; left: 300px; top: 20px; }
  .card--back .deco-ring {
    width: 250px; height: 250px; left: 28px; top: 40px;
    background: var(--emboss); border-color: #262626;
    box-shadow: inset 3px 3px 6px rgba(0,0,0,.45), inset -2px -2px 4px rgba(255,255,255,.06);
  }

  .person { position: absolute; right: 28px; top: 24px; text-align: right; font-family: "Arimo", Arial, sans-serif; }
  .person__name { font-weight: 700; font-size: 17px; letter-spacing: .5px; }
  .person__title { font-size: 12px; color: var(--muted); margin-top: 2px; }

  .brand { position: absolute; left: 28px; top: 108px; display: flex; align-items: center; }
  .brand__dot { width: 52px; height: 52px; border: 3px solid var(--ink); border-radius: 50%; flex: none; }
  .brand__divider { width: 1px; height: 96px; background: var(--muted); margin: 0 16px; flex: none; }
  .brand__name {
    font-family: "Montserrat", sans-serif; font-weight: 500; font-size: 25px;
    letter-spacing: 2.5px; color: var(--ink); text-transform: uppercase; line-height: 1;
  }
  .contacts {
    position: absolute; left: 112px; top: 170px; list-style: none;
    font-family: "Arimo", Arial, sans-serif; font-size: 14px; line-height: 20px;
  }
  .contacts li { display: flex; align-items: center; gap: 7px; }
  .contacts svg { width: 11px; height: 11px; fill: none; stroke: var(--ink); stroke-width: 1.6; flex: none; }
  .rule { position: absolute; left: 112px; top: 258px; width: 400px; height: 1px; background: var(--muted); }
  .address { position: absolute; left: 112px; top: 268px; font-family: "Arimo", Arial, sans-serif; font-size: 14px; }

  .card--back .brand__name { position: absolute; right: 36px; bottom: 60px; font-size: 28px; }
</style>
</head>
<body>
<div class="canvas">
  <section class="card card--front">
    <div class="deco-ring"></div>
    <div class="person">
      <p class="person__name">DANIEL HARPER</p>
      <p class="person__title">Manager</p>
    </div>
    <div class="brand">
      <div class="brand__dot"></div>
      <div class="brand__divider"></div>
      <p class="brand__name">Marble Crest</p>
    </div>
    <ul class="contacts">
      <li><svg viewBox="0 0 12 12"><path d="M3 1 L5 3.5 L4 5 Q5.5 7.5 7 8 L8.5 7 L11 9 L9.5 11 Q4 10 1 2.5 Z"/></svg>555-018-4820</li>
      <li><svg viewBox="0 0 12 12"><rect x="3" y="1" width="6" height="3"/><rect x="1" y="4" width="10" height="5"/><rect x="3" y="7" width="6" height="4"/></svg>555-018-4821</li>
      <li><svg viewBox="0 0 12 12"><rect x="1" y="2.5" width="10" height="7"/><path d="M1 2.5 L6 7 L11 2.5"/></svg>hello@marblecrest.co</li>
      <li><svg viewBox="0 0 12 12"><rect x="1.5" y="1.5" width="9" height="9" rx="2.5"/><circle cx="6" cy="6" r="2.2"/></svg>@marblecrest</li>
    </ul>
    <div class="rule"></div>
    <p class="address">48 Alder Row, Brookfield, ST 01234</p>
  </section>

  <section class="card card--back">
    <div class="deco-ring"></div>
    <p class="brand__name">Marble Crest</p>
  </section>
</div>
</body>
</html>
```